Fresh looking flyer for Vantrel Academy Of Computing

We need a flyer design for our IT school that will be distributed to potential students during our recruitment campaign. We want to feature the following aspects of the school:

-Study IT in a nordic/european way close to your home (design should feel Scandinavian)
-Featuring the dean of the school (photo attached)
-Match the theme of logo (logo attached)
-A potential layout attached as a mockup

CONTENT
* Main Message " LEARN EUROPEAN PROGRAMMING COURSES IN BEKASI"
* Sub Message " 3 MONTH MODULES FROM BEGINNER TO ADVANCED"
* Campaign " ATTEND FREE CLASS & GET 10% OFF COURSE, SIGN UP BETWEEN 7-18MARCH. vantrel.example/free
* Extra info: " GRADUATE AND GET HIRED TO EARN 120 MILLION IDR/YEAR"

End result should be in Adobe Illustrator format.

Target Market(s)

18-30 year old Indonesians interested in IT

Industry/Entity Type

Education

Font styles to use
Sans Serif

Colors
85cae6

Requirements
Must have
• -Photo of the manager
• -Messages as in the project description
• -School logo
• -Nordic look and feel

```html
<!DOCTYPE html>
<html lang="en">
<head>
<meta charset="utf-8">
<title>Vantrel Academy Of Computing – Programming Courses Flyer</title>
<link href="https://fonts.googleapis.com/css2?family=Bebas+Neue&family=Raleway:wght@300;400;600;800&display=swap" rel="stylesheet">
<style>
  :root {
    --navy: #02031c;
    --blue: #12467a;
    --black: #000000;
    --white: #ffffff;
    --stage: #dbe3ec;
    --skin-light: #f1d2bd;
    --shirt: #f4f5f7;
  }
  html, body {
    margin: 0;
    width: 1200px;
    height: 1200px;
    overflow: hidden;
    background: var(--stage);
  }
  .flyer {
    position: absolute;
    left: 50px;
    top: 212px;
    width: 1100px;
    height: 776px;
    display: block;
    box-shadow: 0 10px 30px rgba(0, 20, 50, 0.18);
  }
  .light { font-family: "Raleway", sans-serif; font-weight: 300; }
  .bold { font-family: "Raleway", sans-serif; font-weight: 800; }
  .semi { font-family: "Raleway", sans-serif; font-weight: 600; }
  .condensed { font-family: "Bebas Neue", sans-serif; font-weight: 400; }
  .fill-white { fill: var(--white); }
  .fill-blue { fill: var(--blue); }
  .fill-navy { fill: var(--navy); }
  .fill-black { fill: var(--black); }
</style>
</head>
<body>
<svg class="flyer" viewBox="0 0 1156 815" xmlns="http://www.w3.org/2000/svg">
  <defs>
    <linearGradient id="portrait-tone" x1="0" y1="0" x2="0" y2="1">
      <stop offset="0" stop-color="#c9a877"/>
      <stop offset="0.25" stop-color="var(--skin-light)"/>
      <stop offset="0.6" stop-color="#f6e3d6"/>
      <stop offset="1" stop-color="var(--shirt)"/>
    </linearGradient>
  </defs>

  <!-- base sheet -->
  <rect class="fill-white" width="1156" height="815"/>

  <!-- top edge bars -->
  <rect class="fill-black" x="0" y="0" width="713" height="20"/>
  <rect class="fill-blue" x="733" y="0" width="423" height="20"/>

  <!-- geometric panels -->
  <polygon class="fill-blue" points="0,20 258,20 0,278"/>
  <polygon class="fill-blue" points="650,20 868,188 643,218"/>
  <polygon class="fill-navy" points="0,296 1156,153 1156,560 760,560 0,512"/>
  <polygon class="fill-blue" points="618,618 880,560 880,795 618,795"/>
  <polygon class="fill-blue" points="1090,360 1156,300 1156,560 1100,470"/>

  <!-- dean portrait area -->
  <path class="portrait" role="img" aria-label="Portrait photo of the school's dean in glasses and a white shirt"
        d="M880,230 Q880,170 1000,172 Q1125,175 1130,260 L1130,420 Q1140,470 1156,500 L1156,795 L730,795 Q760,560 930,520 L930,470 Q880,430 880,330 Z"
        fill="url(#portrait-tone)"/>

  <!-- bottom edge bars -->
  <rect class="fill-blue" x="0" y="795" width="423" height="20"/>
  <rect class="fill-black" x="443" y="795" width="713" height="20"/>

  <!-- school name -->
  <g class="school-name">
    <circle class="fill-blue" cx="438" cy="82" r="34"/>
    <text class="semi fill-blue" x="438" y="172" font-size="30" text-anchor="middle">VANTREL ACADEMY</text>
    <text class="semi fill-blue" x="438" y="210" font-size="30" text-anchor="middle">OF COMPUTING</text>
  </g>

  <!-- main message -->
  <g class="main-message">
    <text class="light fill-white" x="438" y="308" font-size="33" text-anchor="middle">LEARN EUROPEAN</text>
    <polygon class="fill-blue" points="0,318 733,318 753,374 0,374"/>
    <text class="bold fill-white" x="438" y="367" font-size="54" text-anchor="middle" letter-spacing="1">PROGRAMMING</text>
    <text class="light fill-white" x="428" y="422" font-size="48" text-anchor="middle">COURSES IN BEKASI</text>
  </g>

  <!-- sub message -->
  <g class="sub-message">
    <line x1="160" y1="465" x2="710" y2="465" stroke="#ffffff" stroke-opacity="0.4" stroke-width="1"/>
    <text class="light fill-white" x="434" y="499" font-size="28" text-anchor="middle">3 MONTH MODULES FROM BEGINNER TO ADVANCED</text>
    <line x1="160" y1="512" x2="710" y2="512" stroke="#ffffff" stroke-opacity="0.4" stroke-width="1"/>
  </g>

  <!-- campaign ribbon -->
  <g class="campaign-ribbon">
    <polygon class="fill-blue" points="198,560 670,560 658,588 670,616 198,616 212,588"/>
    <text class="condensed fill-white" x="434" y="607" font-size="48" text-anchor="middle">ATTEND FREE CLASS &amp;</text>
  </g>

  <!-- discount block -->
  <g class="discount">
    <text class="bold fill-navy" font-size="68" text-anchor="middle" transform="translate(166 700) rotate(-90)">GET</text>
    <rect class="fill-blue" x="176" y="633" width="124" height="77"/>
    <text class="condensed fill-white" x="238" y="705" font-size="86" text-anchor="middle">10%</text>
    <text class="light fill-navy" x="174" y="767" font-size="62">OFF</text>
    <text class="bold fill-blue" font-size="30" text-anchor="middle" transform="translate(330 700) rotate(-90)">COURSE,</text>
  </g>

  <!-- sign-up details -->
  <g class="signup">
    <text class="light fill-navy" x="478" y="672" font-size="28" text-anchor="middle">SIGN UP BETWEEN</text>
    <polygon class="fill-navy" points="338,678 1156,678 1156,720 338,720 350,699"/>
    <text class="condensed fill-white" x="478" y="716" font-size="48" text-anchor="middle">7-18MARCH.</text>
    <text class="semi fill-navy" x="478" y="752" font-size="24" text-anchor="middle">vantrel.example/free</text>
  </g>

  <!-- salary starburst -->
  <g class="salary-badge" transform="translate(820 660)">
    <polygon class="fill-blue" stroke="#ffffff" stroke-width="6" stroke-linejoin="miter"
             points="140,0 104.3,28 121.2,70 76.4,76.4 70,121.2 28,104.3 0,140 -28,104.3 -70,121.2 -76.4,76.4 -121.2,70 -104.3,28 -140,0 -104.3,-28 -121.2,-70 -76.4,-76.4 -70,-121.2 -28,-104.3 0,-140 28,-104.3 70,-121.2 76.4,-76.4 121.2,-70 104.3,-28"/>
    <text class="light fill-white" x="0" y="-35" font-size="15" text-anchor="middle">GRADUATE AND GET</text>
    <line x1="-78" y1="-20" x2="-62" y2="-20" stroke="#ffffff" stroke-width="1.5"/>
    <text class="light fill-white" x="0" y="-15" font-size="15" text-anchor="middle">HIRED TO EARN</text>
    <line x1="62" y1="-20" x2="78" y2="-20" stroke="#ffffff" stroke-width="1.5"/>
    <text class="condensed fill-white" x="0" y="23" font-size="44" text-anchor="middle">120 MILLION</text>
    <line x1="-80" y1="30" x2="80" y2="30" stroke="#ffffff" stroke-width="1.5"/>
    <text class="light fill-white" x="0" y="46" font-size="14" text-anchor="middle">IDR/YEAR</text>
    <line x1="-80" y1="52" x2="80" y2="52" stroke="#ffffff" stroke-width="1"/>
  </g>
</svg>
</body>
</html>
```